KRT business cards

I need a Business card design for my self. I am behavior analyst owner of a new company based in Miami. We offer Applied Behavior Analysis (ABA) services to individuals with developmental disabilities.

Business

```html
<!DOCTYPE html>
<html lang="en">
<head>
<meta charset="utf-8">
<title>KRT Business Cards</title>
<link rel="stylesheet" href="https://fonts.googleapis.com/css2?family=Montserrat:wght@400;500;700&display=swap">
<style>
  :root {
    --navy: #124b7c;
    --navy-deep: #0f4372;
    --green: #4a9a3a;
    --card-white: #f3f3f3;
    --backdrop: #d9d6d1;
    --light-text: #e6edf4;
  }
  * { margin: 0; padding: 0; box-sizing: border-box; }
  html, body { width: 1200px; height: 900px; overflow: hidden; }
  body {
    background: var(--backdrop);
    font-family: "Montserrat", sans-serif;
    display: flex;
    flex-direction: column;
    align-items: center;
    justify-content: center;
    gap: 50px;
  }
  .card {
    position: relative;
    width: 630px;
    height: 360px;
    background: var(--card-white);
    box-shadow: 0 8px 22px rgba(0,0,0,0.18);
    overflow: hidden;
  }

  /* Front side */
  .card-front .brand-mark {
    position: absolute;
    left: 150px;
    top: 130px;
    display: flex;
    align-items: center;
    gap: 12px;
  }
  .brand-dot {
    width: 26px; height: 26px;
    border-radius: 50%;
    background: var(--green);
  }
  .brand-name {
    font-weight: 700;
    font-size: 62px;
    color: var(--navy);
    letter-spacing: 2px;
    line-height: 1;
  }
  .service-list {
    position: absolute;
    left: 350px;
    top: 132px;
    list-style: none;
  }
  .service-list li {
    display: flex;
    align-items: center;
    gap: 9px;
    font-weight: 700;
    font-size: 14px;
    color: var(--navy);
    letter-spacing: 0.6px;
    margin-bottom: 8px;
  }
  .service-list svg { width: 12px; height: 12px; flex: none; }

  /* Back side */
  .card-back .wave { position: absolute; inset: 0; width: 100%; height: 100%; }
  .card-back .brand-mark {
    position: absolute;
    left: 342px;
    top: 72px;
    display: flex;
    flex-direction: column;
    align-items: center;
    gap: 6px;
  }
  .card-back .brand-dot { width: 18px; height: 18px; }
  .card-back .brand-name { font-size: 40px; }
  .contact {
    position: absolute;
    left: 46px;
    top: 135px;
    color: var(--light-text);
  }
  .contact-name {
    font-weight: 500;
    font-size: 17px;
    letter-spacing: 1.2px;
    margin-bottom: 6px;
  }
  .contact-title {
    font-size: 10.5px;
    letter-spacing: 0.8px;
    margin-bottom: 16px;
  }
  .contact-line {
    display: flex;
    align-items: center;
    gap: 10px;
    font-size: 10.5px;
    letter-spacing: 0.8px;
    margin-bottom: 10px;
  }
  .contact-line svg { width: 11px; height: 11px; flex: none; }
</style>
</head>
<body>

  <section class="card card-front" aria-label="Card front">
    <div class="brand-mark">
      <span class="brand-dot"></span>
      <span class="brand-name">KRT</span>
    </div>
    <ul class="service-list">
      <li><svg viewBox="0 0 12 12"><path d="M1.5 6.5 L4.5 9.5 L10.5 2.5" fill="none" stroke="#4a9a3a" stroke-width="2"/></svg>Applied Behavior Analysis</li>
      <li><svg viewBox="0 0 12 12"><path d="M1.5 6.5 L4.5 9.5 L10.5 2.5" fill="none" stroke="#4a9a3a" stroke-width="2"/></svg>Parent/Teacher Training</li>
      <li><svg viewBox="0 0 12 12"><path d="M1.5 6.5 L4.5 9.5 L10.5 2.5" fill="none" stroke="#4a9a3a" stroke-width="2"/></svg>Social Skills Training</li>
      <li><svg viewBox="0 0 12 12"><path d="M1.5 6.5 L4.5 9.5 L10.5 2.5" fill="none" stroke="#4a9a3a" stroke-width="2"/></svg>Tutoring</li>
    </ul>
  </section>

  <section class="card card-back" aria-label="Card back">
    <svg class="wave" viewBox="0 0 630 360" preserveAspectRatio="none">
      <path d="M0 62 Q 390 95 560 360" fill="none" stroke="#4a9a3a" stroke-width="4"/>
      <path d="M0 68 Q 385 102 552 360 L0 360 Z" fill="#124b7c"/>
      <circle cx="430" cy="290" r="70" fill="#0f4372"/>
    </svg>
    <div class="brand-mark">
      <span class="brand-dot"></span>
      <span class="brand-name">KRT</span>
    </div>
    <div class="contact">
      <p class="contact-name">Marisol Vega, B.A.</p>
      <p class="contact-title">Board Certified Asst. Behavior Analyst (BCaBA)</p>
      <p class="contact-line">
        <svg viewBox="0 0 12 12"><path d="M2 1 L4.5 1 L5.5 4 L4 5 Q5 7.5 7 8 L8 6.5 L11 7.5 L11 10 Q6 11.5 2.5 7.5 Q0.5 4.5 2 1 Z" fill="#4a9a3a"/></svg>
        786-555-0142
      </p>
      <p class="contact-line">
        <svg viewBox="0 0 12 12"><rect x="0.5" y="2" width="11" height="8" fill="none" stroke="#4a9a3a" stroke-width="1.3"/><path d="M0.5 2 L6 6.5 L11.5 2" fill="none" stroke="#4a9a3a" stroke-width="1.3"/></svg>
        mvega.aba@mail.com
      </p>
    </div>
  </section>

</body>
</html>
```